Corvella Santoro Winery 2023 Label

We are just about to bottle our very first Napa Valley Cabernet Sauvignon and need label ideas

Target Market(s)

Cab drinkers who like Napa California Cabs

Industry/Entity Type

Wine Making

Logo Text

Corvella Santoro 2023 Napa Estate Grown Cabernet Sauvignon

Requirements
Must have
• Winery Name, year of vintage and Napa Estate Cab
Nice to have
• If using the initials C and S use gold letters on black or red background

```html
<!DOCTYPE html>
<html lang="en">
<head>
<meta charset="utf-8">
<title>Corvella Santoro 2023 Cabernet Sauvignon Label</title>
<link rel="stylesheet" href="https://fonts.googleapis.com/css2?family=Cinzel:wght@400;500;600&family=Arimo:wght@400&display=swap">
<style>
  :root {
    --label-black: #0b0b0b;
    --label-shade: #161616;
    --gold-light: #f3d27a;
    --gold-mid: #c9962e;
    --gold-deep: #8a6116;
    --olive-gold: #9a8040;
    --copper: #d36a3c;
    --copper-deep: #a8472a;
  }
  html, body {
    margin: 0;
    padding: 0;
    width: 1200px;
    height: 1200px;
    overflow: hidden;
    background: var(--label-black);
  }
  .label {
    position: relative;
    width: 1200px;
    height: 1200px;
    background: radial-gradient(ellipse at 50% 40%, var(--label-shade) 0%, var(--label-black) 70%);
  }
  .gold {
    background: linear-gradient(180deg, var(--gold-light) 0%, var(--gold-mid) 55%, var(--gold-deep) 100%);
    -webkit-background-clip: text;
    background-clip: text;
    color: transparent;
  }
  .winery-name {
    position: absolute;
    left: 0;
    width: 1200px;
    text-align: center;
    margin: 0;
    font-family: "Cinzel", serif;
    font-weight: 500;
    font-size: 150px;
    line-height: 1;
    letter-spacing: 2px;
  }
  .winery-name--first { top: 462px; }
  .winery-name--second { top: 608px; }
  .trademark {
    font-family: "Cinzel", serif;
    font-size: 18px;
    vertical-align: top;
    position: relative;
    top: 14px;
    letter-spacing: 0;
  }
  .divider-ornament {
    position: absolute;
    left: 335px;
    top: 752px;
    width: 491px;
    height: 56px;
    background: linear-gradient(90deg, rgba(201,150,46,0) 0%, rgba(201,150,46,0.55) 50%, rgba(201,150,46,0) 100%);
  }
  .vintage-row {
    position: absolute;
    left: 0;
    top: 826px;
    width: 1200px;
    height: 50px;
  }
  .vintage-rule {
    position: absolute;
    top: 24px;
    height: 2px;
    background: var(--gold-mid);
  }
  .vintage-rule--left { left: 301px; width: 190px; }
  .vintage-rule--right { left: 689px; width: 193px; }
  .vintage {
    position: absolute;
    left: 0;
    width: 1200px;
    top: 2px;
    text-align: center;
    font-family: "Cinzel", serif;
    font-weight: 500;
    font-size: 40px;
    letter-spacing: 9px;
    line-height: 1;
  }
  .estate-line {
    position: absolute;
    left: 0;
    width: 1200px;
    top: 893px;
    text-align: center;
    font-family: "Arimo", sans-serif;
    font-size: 33px;
    line-height: 1;
    background: linear-gradient(90deg, var(--gold-mid) 0%, var(--olive-gold) 100%);
    -webkit-background-clip: text;
    background-clip: text;
    color: transparent;
  }
  .varietal {
    position: absolute;
    left: 0;
    width: 1200px;
    top: 946px;
    text-align: center;
    font-family: "Cinzel", serif;
    font-weight: 500;
    font-size: 44px;
    letter-spacing: 5px;
    line-height: 1;
    background: linear-gradient(90deg, var(--copper) 0%, var(--copper-deep) 100%);
    -webkit-background-clip: text;
    background-clip: text;
    color: transparent;
  }
</style>
</head>
<body>
  <main class="label">
    <h1 class="winery-name winery-name--first gold">Corvella</h1>
    <h1 class="winery-name winery-name--second gold">Santoro<span class="trademark">TM</span></h1>
    <div class="divider-ornament" role="img" aria-label="Gold foil decorative divider ornament"></div>
    <div class="vintage-row">
      <span class="vintage-rule vintage-rule--left"></span>
      <span class="vintage gold">2023</span>
      <span class="vintage-rule vintage-rule--right"></span>
    </div>
    <p class="estate-line" style="margin:0">ESTATE GROWN NAPA VALLEY</p>
    <p class="varietal" style="margin:0">Cabernet Sauvignon</p>
  </main>
</body>
</html>
```